A3 Event Poster for School Fundraiser

We are looking for a bold, engaging, and professional A3 poster design to promote a special school fundraising event. A top athlete will be visiting a primary school to inspire children, encourage participation in sport, and help launch a fundraising initiative to raise money for new PE/sports equipment for the school.

The poster will be displayed prominently outside the school and shared with parents and families. Its purpose is to generate excitement, explain the event quickly, and encourage parents/families to sponsor and get involved.

We work with about 50 different athletes so will need the design to be easy to alter the picture of the athlete/name etc so it can be replicated across the different athletes.

Target Market(s)

Priamary School Parents/Communities

Industry/Entity Type

Education

Other font styles liked:
• The logo font is Rajdhani. ‘Plume’ is bold, ‘Harbours’ is semibold and the strapline is regular.

Requirements
Must have
• Space for the Event Date (that school can write in themselves), A picture of the visiting athlete and their bio (with ability to easily change)
Nice to have
• Bold, eye-catching

```html
<!DOCTYPE html>
<html lang="en">
<head>
<meta charset="utf-8">
<title>Plume Harbours – Athlete Visit Poster</title>
<link rel="stylesheet" href="https://fonts.googleapis.com/css2?family=Barlow:ital,wght@0,700;1,500&family=Barlow+Semi+Condensed:wght@700&family=Open+Sans:wght@400&family=Rajdhani:wght@400;500;600;700&display=swap">
<style>
  :root {
    --page-bg: #ececec;
    --white: #ffffff;
    --red-bright: #d8203c;
    --red-deep: #5a0010;
    --purple: #4a1660;
    --purple-dark: #350b49;
    --purple-accent: #8a3aa6;
    --brand-purple: #6b2a86;
    --brand-red: #d01f3c;
    --photo-top: #6a2b5a;
    --photo-bottom: #3d1150;
  }
  * { box-sizing: border-box; margin: 0; padding: 0; }
  html, body {
    width: 1200px; height: 900px; overflow: hidden;
    background: var(--page-bg);
  }
  .poster {
    position: absolute; left: 320px; top: 19px;
    width: 560px; height: 862px;
    background: var(--white);
    overflow: hidden;
    box-shadow: 0 4px 14px rgba(0,0,0,0.18);
  }
  .poster-shapes { position: absolute; inset: 0; width: 560px; height: 862px; }

  .brand {
    position: absolute; left: 160px; top: 22px;
    display: flex; align-items: center; gap: 8px;
  }
  .brand-mark { width: 38px; height: 38px; border-radius: 50%; background: var(--brand-red); }
  .brand-name {
    font-family: "Rajdhani", sans-serif; font-weight: 600;
    font-size: 46px; line-height: 1; color: var(--brand-purple);
  }
  .brand-strap {
    position: absolute; left: 206px; top: 70px;
    font-family: "Rajdhani", sans-serif; font-weight: 400;
    font-size: 15px; color: var(--brand-purple);
  }

  .athlete-photo {
    position: absolute; left: 367px; top: 80px;
    width: 193px; height: 252px;
    background: linear-gradient(180deg, var(--photo-top) 0%, var(--photo-bottom) 100%);
  }

  .headline {
    position: absolute; left: 27px; top: 186px;
    font-family: "Rajdhani", sans-serif; font-weight: 500;
    font-size: 30px; line-height: 35px; color: var(--white);
  }
  .role-label {
    position: absolute; left: 27px; top: 268px;
    font-family: "Rajdhani", sans-serif; font-weight: 700;
    font-size: 27px; line-height: 44px; color: var(--white);
  }
  .appeal {
    position: absolute; left: 27px; top: 334px;
    font-family: "Rajdhani", sans-serif; font-weight: 700;
    font-size: 27px; line-height: 36px; color: var(--white);
  }
  .athlete-name {
    position: absolute; right: 33px; top: 342px;
    font-family: "Barlow", sans-serif; font-weight: 700;
    font-size: 26px; line-height: 32px; color: var(--white); text-align: right;
  }
  .athlete-bio {
    position: absolute; right: 33px; top: 376px; width: 200px;
    font-family: "Barlow", sans-serif; font-style: italic; font-weight: 500;
    font-size: 13.5px; line-height: 23.3px; color: var(--white); text-align: right;
  }
  .motto {
    position: absolute; left: 90px; top: 446px;
    transform-origin: 0 0; transform: rotate(33.7deg);
    font-family: "Open Sans", sans-serif; font-weight: 400;
    font-size: 24px; color: var(--white); white-space: nowrap;
    display: flex; align-items: center; gap: 6px;
  }
  .motto-dot {
    display: inline-block; width: 13px; height: 13px;
    border-radius: 50%; background: var(--white);
  }
  .event-date {
    position: absolute; left: 27px; top: 639px;
    font-family: "Barlow Semi Condensed", sans-serif; font-weight: 700;
    font-size: 34px; line-height: 43px; color: var(--white);
  }
  .tagline {
    position: absolute; left: 27px; top: 740px;
    font-family: "Barlow", sans-serif; font-style: italic; font-weight: 500;
    font-size: 26px; line-height: 36px; color: var(--white);
  }
</style>
</head>
<body>
<main class="poster">
  <svg class="poster-shapes" viewBox="0 0 825 1270" preserveAspectRatio="none" aria-hidden="true">
    <defs>
      <linearGradient id="redField" x1="0" y1="0" x2="1" y2="1">
        <stop offset="0" stop-color="#d8203c"/>
        <stop offset="0.55" stop-color="#b0142a"/>
        <stop offset="1" stop-color="#5a0010"/>
      </linearGradient>
      <linearGradient id="purpleField" x1="0" y1="0" x2="1" y2="1">
        <stop offset="0" stop-color="#3a0d4f"/>
        <stop offset="1" stop-color="#4f1c68"/>
      </linearGradient>
      <linearGradient id="roleBand" x1="0" y1="0" x2="1" y2="0">
        <stop offset="0" stop-color="#4a1660"/>
        <stop offset="0.7" stop-color="#5c1a5a"/>
        <stop offset="1" stop-color="#7a2050" stop-opacity="0.6"/>
      </linearGradient>
    </defs>
    <polygon class="upper-purple" points="410,262 825,72 825,520" fill="#4a1660"/>
    <polygon class="red-field" points="0,5 825,515 825,1170 0,645" fill="url(#redField)"/>
    <polygon class="lower-purple" points="0,645 825,1170 825,1270 0,1270" fill="url(#purpleField)"/>
    <polygon class="white-stripe" points="310,842 825,1170 825,1228 660,1110 660,1070 310,862" fill="#ffffff"/>
    <polygon class="role-band" points="0,395 500,395 462,465 0,465" fill="url(#roleBand)"/>
    <polygon class="accent-bar" points="8,670 75,712 75,742 8,700" fill="#8a3aa6"/>
    <polygon class="accent-bar" points="75,745 200,825 200,850 75,770" fill="#8a3aa6"/>
    <polygon class="accent-bar" points="250,860 375,940 375,965 250,885" fill="#8a3aa6"/>
  </svg>

  <div class="brand">
    <span class="brand-mark"></span>
    <span class="brand-name">PlumeHarbours</span>
  </div>
  <div class="brand-strap">Inspiring every child</div>

  <div class="athlete-photo" role="img" aria-label="Photo of the visiting athlete"></div>

  <h1 class="headline">Inspirational Athlete<br>Visiting Our School</h1>
  <p class="role-label">Olympic Volleyball Player</p>
  <p class="appeal">“Help Us Raise Funds<br>For New Sports Equipment”</p>

  <h2 class="athlete-name">MARCUS ADEYEMI</h2>
  <p class="athlete-bio">is a dynamic English<br>volleyball player and coach,<br>known for his<br>leadership on and off the<br>court and his<br>passion for inspiring the<br>next generation<br>through sport.</p>

  <p class="motto"><span class="motto-dot"></span>Be inspired <span class="motto-dot"></span>Make a difference <span class="motto-dot"></span>Get Active</p>

  <p class="event-date">SUNDAY<br>APRIL 00TH | 0 PM</p>
  <p class="tagline">Inspiring every child to lead an active<br>resilient and healthy life</p>
</main>
</body>
</html>
```